Caldrow Supplies Business Card

Professional business card that stand out to our potential customers. Front and back with clean modern design

Industry/Entity Type

Oil and gas

Contact Information for Business Card

Name, address, website , office phone and cell number

Requirements
Must have
• Editable files for each employee

```html
<!DOCTYPE html>
<html lang="en">
<head>
<meta charset="utf-8">
<title>Caldrow Supplies Business Card</title>
<link rel="stylesheet" href="https://fonts.googleapis.com/css2?family=Lexend:wght@400;500;800&family=Fira+Sans:wght@600&display=swap">
<style>
  :root {
    --bg-top: #1a6aa9;
    --bg-mid: #0d3d8f;
    --bg-bottom: #040c5e;
    --card-white: #ffffff;
    --card-dark: #131c2b;
    --pattern-dark: #182234;
    --brand-red: #f70f0f;
    --brand-cyan: #06b1d4;
    --ink: #161616;
    --white: #ffffff;
  }
  * { margin: 0; padding: 0; box-sizing: border-box; }
  html, body { width: 1038px; height: 1200px; overflow: hidden; }
  body {
    position: relative;
    background: linear-gradient(180deg, var(--bg-top) 0%, var(--bg-mid) 50%, var(--bg-bottom) 100%);
    font-family: "Lexend", Arial, sans-serif;
    color: var(--ink);
  }
  .card { position: absolute; overflow: hidden; }
  .card-front { left: 89px; top: 92px; width: 852px; height: 488px; background: var(--card-white); }
  .card-back { left: 86px; top: 615px; width: 858px; height: 491px; background: var(--card-dark); }

  .stripe { position: absolute; left: 0; bottom: 0; width: 100%; height: 18px; }

  .person-name { position: absolute; left: 47px; top: 192px; font-size: 35px; font-weight: 500; line-height: 1; letter-spacing: 0.2px; }
  .person-role { position: absolute; left: 47px; top: 241px; font-size: 18px; font-weight: 500; line-height: 1; color: var(--brand-red); }
  .divider { position: absolute; left: 26px; top: 277px; width: 812px; height: 1.5px; background: var(--brand-red); }

  .contact-list { position: absolute; left: 49px; top: 304px; list-style: none; }
  .contact-item { display: flex; align-items: center; height: 24px; font-size: 19px; font-weight: 400; }
  .contact-item + .contact-item { margin-top: 20px; }
  .contact-item:nth-child(3) { margin-top: 17px; }
  .contact-icon { width: 20px; height: 20px; margin-right: 13px; flex: none; }

  .address { position: absolute; right: 46px; top: 358px; text-align: right; font-size: 18px; font-weight: 400; line-height: 30px; font-style: normal; }

  .brand-lockup { position: absolute; right: 45px; top: 218px; display: flex; align-items: center; gap: 10px; }
  .brand-square { width: 22px; height: 22px; background: var(--brand-red); }
  .brand-name { font-size: 24px; font-weight: 800; line-height: 1; color: var(--brand-red); text-transform: uppercase; }

  .back-pattern { position: absolute; left: 0; top: 0; width: 100%; height: 340px;
    background: linear-gradient(180deg, var(--pattern-dark) 0%, var(--card-dark) 100%); }
  .back-brand { position: absolute; right: 64px; top: 282px; font-size: 20px; font-weight: 800; line-height: 1; color: var(--white); text-transform: uppercase; }
  .tagline { position: absolute; right: 64px; top: 366px; font-family: "Fira Sans", Arial, sans-serif; font-weight: 600; font-size: 28px; line-height: 1; color: var(--white); letter-spacing: 0.3px; }
</style>
</head>
<body>

<section class="card card-front">
  <div class="brand-lockup">
    <span class="brand-square"></span>
    <span class="brand-name">Caldrow Supplies</span>
  </div>

  <h1 class="person-name">Owen Hartley</h1>
  <p class="person-role">Founder, Caldrow Supplies</p>
  <div class="divider"></div>

  <ul class="contact-list">
    <li class="contact-item">
      <svg class="contact-icon" viewBox="0 0 20 20" aria-hidden="true">
        <path d="M1 8 L10 2 L19 8 V17 a1 1 0 0 1 -1 1 H2 a1 1 0 0 1 -1 -1 Z" fill="var(--brand-cyan)"/>
        <path d="M3 9 L10 13.5 L17 9" fill="none" stroke="#fff" stroke-width="1.6"/>
      </svg>
      sales@caldrowsupplies.com
    </li>
    <li class="contact-item">
      <svg class="contact-icon" viewBox="0 0 20 20" aria-hidden="true">
        <rect x="0" y="0" width="20" height="20" rx="3" fill="var(--brand-cyan)"/>
        <path d="M6 4 L8 4 L9 7.5 L7.6 8.8 C8.4 10.6 9.6 11.8 11.2 12.5 L12.5 11 L16 12 L16 14.2 C16 15 15.3 15.6 14.5 15.5 C9 15 5 11 4.5 5.5 C4.4 4.7 5.1 4 6 4 Z" fill="#fff"/>
      </svg>
      (555)410-0287
    </li>
    <li class="contact-item">
      <svg class="contact-icon" viewBox="0 0 20 20" aria-hidden="true">
        <circle cx="10" cy="10" r="9.5" fill="var(--brand-cyan)"/>
        <path d="M5 5 C7 4 9 6 8 8 C7 10 4 9 4 12 M12 3.5 C11 6 14 6 15 8 C16 10 13 12 14 15.5" fill="none" stroke="#fff" stroke-width="1.6"/>
      </svg>
      www.caldrowsupplies.com
    </li>
  </ul>

  <address class="address">
    18 N.Larkmont Suite 6<br>
    Brenvale, Tx 79000
  </address>

  <svg class="stripe" viewBox="0 0 852 18" preserveAspectRatio="none" aria-hidden="true">
    <polygon points="0,0 449,0 443,18 0,18" fill="var(--brand-red)"/>
    <polygon points="452,0 852,0 852,18 446,18" fill="var(--brand-cyan)"/>
  </svg>
</section>

<section class="card card-back">
  <div class="back-pattern" role="img" aria-label="Repeating brand pattern in dark navy"></div>
  <p class="back-brand">Caldrow Supplies</p>
  <p class="tagline">BUILT FOR THE BASIN.</p>

  <svg class="stripe" viewBox="0 0 858 18" preserveAspectRatio="none" aria-hidden="true">
    <polygon points="0,0 451,0 445,18 0,18" fill="var(--brand-red)"/>
    <polygon points="454,0 858,0 858,18 448,18" fill="var(--brand-cyan)"/>
  </svg>
</section>

</body>
</html>
```